Mortgage Loan officer needs clean/modern business card design

Looking for a clean, modern 2-sided business card design. We like the earth tones used in our logo and website http://vukarhome-lending.example . Would also like to incorporate: 1) Something special to make our card stand out - a pop of color or embossed logo, for instance and 2) please include "Mortgage Loans" "Reverse Mortgages" "Private Money Loans" on back of card with the logo.

Front: Needs to include agent/company license info - see website. Agent name: Niall Hargrove

Here are fonts and colors used for our logo:
Font: Avenir Next
Colors:
#2c3539 - Dark Gray
#576870 - Light Gray
#ffffff - Background White

Target Market(s)

Prospects and current clients. Will also be distributing to people in professional network (attorneys and CPAs)

Industry/Entity Type

Business

Contact Information for Business Card

Include agent name, contact info, website on front, licensing info for agent an company. Logo and services offered on back

Font styles to use
Other font styles liked:
• Avenir Next

Requirements
Must have
• See project description
Should not have
• Nothing cheesy

```html
<!DOCTYPE html>
<html lang="en">
<head>
<meta charset="utf-8">
<title>Niall Hargrove – Business Card</title>
<link href="https://fonts.googleapis.com/css2?family=Nunito+Sans:wght@400;600;800&display=swap" rel="stylesheet">
<style>
  :root {
    --dark-gray: #2c3539;
    --light-gray: #576870;
    --white: #ffffff;
    --stage: #e6e8e9;
    --line: rgba(255,255,255,0.55);
  }
  * { box-sizing: border-box; margin: 0; padding: 0; }
  html, body {
    width: 1200px; height: 900px; overflow: hidden;
    background: var(--stage);
    font-family: "Nunito Sans", "Avenir Next", sans-serif;
  }
  .canvas { position: relative; width: 1200px; height: 900px; }

  .card {
    position: absolute; width: 600px; height: 343px; overflow: hidden;
    box-shadow: 0 6px 18px rgba(0,0,0,0.18);
  }

  /* ---------- Back side ---------- */
  .card-back { left: 100px; top: 90px; background: var(--dark-gray); }
  .card-back .pattern-field {
    position: absolute; inset: 0;
    background: linear-gradient(135deg, #303a3e 0%, #2c3539 60%, #293236 100%);
  }
  .logo-seal {
    position: absolute; border-radius: 50%;
    display: flex; align-items: center; justify-content: center; text-align: center;
    font-weight: 600; line-height: 1.2; letter-spacing: 0.02em;
  }
  .card-back .logo-seal {
    left: 182px; top: 112px; width: 122px; height: 122px;
    border: 1.5px solid var(--line); color: var(--white); font-size: 15px;
  }
  .service-list {
    position: absolute; left: 262px; top: 242px; list-style: none;
    color: var(--white); font-size: 17px; letter-spacing: 0.03em; line-height: 1.5;
  }
  .service-list li { display: flex; align-items: center; gap: 10px; }
  .service-list svg { width: 12px; height: 12px; flex: none; }

  /* ---------- Front side ---------- */
  .card-front { left: 500px; top: 470px; background: var(--white); }
  .name-marker {
    position: absolute; left: 0; top: 106px; width: 28px; height: 12px;
    background: var(--dark-gray);
  }
  .agent-block {
    position: absolute; left: 40px; top: 96px;
    color: var(--dark-gray); font-size: 15.5px; line-height: 1.45; letter-spacing: 0.01em;
  }
  .agent-name { font-weight: 800; color: var(--light-gray); letter-spacing: 0.04em; }
  .agent-title { font-weight: 400; }
  .contact-band {
    position: absolute; left: 0; top: 170px; width: 540px; height: 148px;
    background: var(--dark-gray);
  }
  .card-front .logo-seal {
    right: 22px; top: 84px; width: 132px; height: 132px;
    background: var(--white); border: 2px solid var(--light-gray);
    box-shadow: 0 0 0 5px var(--white);
    color: var(--dark-gray); font-size: 15px;
  }
  .contact-list {
    position: absolute; left: 28px; top: 186px; list-style: none;
    color: var(--white); font-size: 15.5px; line-height: 1.5; letter-spacing: 0.02em;
  }
  .contact-list li { display: flex; align-items: center; gap: 12px; }
  .contact-list svg { width: 12px; height: 12px; flex: none; }
  .contact-list .address { padding-left: 24px; }
</style>
</head>
<body>
<main class="canvas">

  <section class="card card-back" aria-label="Business card back">
    <div class="pattern-field" role="img" aria-label="Faint pattern of thin overlapping circles on dark gray"></div>
    <div class="logo-seal">The Hargrove<br>Group</div>
    <ul class="service-list">
      <li><svg viewBox="0 0 12 12"><circle cx="6" cy="6" r="5.5" fill="#fff"/><path d="M3.3 6.2l1.8 1.7 3.6-3.7" stroke="#2c3539" stroke-width="1.4" fill="none"/></svg>MORTGAGE LOANS</li>
      <li><svg viewBox="0 0 12 12"><circle cx="6" cy="6" r="5.5" fill="#fff"/><path d="M3.3 6.2l1.8 1.7 3.6-3.7" stroke="#2c3539" stroke-width="1.4" fill="none"/></svg>REVERSE MORTGAGES</li>
      <li><svg viewBox="0 0 12 12"><circle cx="6" cy="6" r="5.5" fill="#fff"/><path d="M3.3 6.2l1.8 1.7 3.6-3.7" stroke="#2c3539" stroke-width="1.4" fill="none"/></svg>PRIVATE MONEY LOANS</li>
    </ul>
  </section>

  <section class="card card-front" aria-label="Business card front">
    <div class="name-marker"></div>
    <div class="agent-block">
      <p><span class="agent-name">NIALL HARGROVE</span> <span class="agent-title">| Loan Officer</span></p>
      <p>NMLS:482915 DRE:01738260</p>
      <p>CO: DRE:01526947/NMLS:604718</p>
    </div>
    <div class="contact-band"></div>
    <div class="logo-seal">The Hargrove<br>Group</div>
    <ul class="contact-list">
      <li><svg viewBox="0 0 12 12"><rect x="3" y="0.5" width="6" height="11" rx="1.2" fill="none" stroke="#fff" stroke-width="1.2"/><circle cx="6" cy="9.5" r="0.7" fill="#fff"/></svg>650-555-0147</li>
      <li><svg viewBox="0 0 12 12"><path d="M2.5 1h2.2l1 2.6-1.3 1a6 6 0 0 0 3 3l1-1.3 2.6 1v2.2c0 .6-.5 1-1 1A9.5 9.5 0 0 1 1.5 2c0-.5.4-1 1-1z" fill="#fff"/></svg>408-555-0192 x138</li>
      <li><svg viewBox="0 0 12 12"><circle cx="6" cy="6" r="5" fill="none" stroke="#fff" stroke-width="1"/><ellipse cx="6" cy="6" rx="2.2" ry="5" fill="none" stroke="#fff" stroke-width="0.9"/><path d="M1 6h10M2 3.5h8M2 8.5h8" stroke="#fff" stroke-width="0.8"/></svg>www.vukarhome-lending.example</li>
      <li class="address">2840 Meridian Court, Suite 210</li>
      <li class="address">San Jose, CA 95128</li>
    </ul>
  </section>

</main>
</body>
</html>
```